Healthcare IT company looking for business card design

We develop IT systems for healthcare that significantly reduces cost and improves quality.

We want a business card design that is professional and clean, and using the colors in our logo.

Target Market(s)

Doctors and decision makers in the healthcare industry

Industry/Entity Type

Healthcare

Contact Information for Business Card

It should include
Name and title, address, telephone

Tobias Vrenholt, CEO
+46 712 418257
tobias@kelvaro.se

Font styles to use
Serif

Colors
0355a3
ed282f

Requirements
Must have
• Clean design
• Professional feel
Nice to have
• N/A
Should not have
• N/A

```html
<!DOCTYPE html>
<html lang="en">
<head>
<meta charset="utf-8">
<title>Kelvaro Business Card</title>
<link rel="stylesheet" href="https://fonts.googleapis.com/css2?family=Nunito+Sans:wght@700;800&family=Open+Sans:wght@400;600;700&display=swap">
<style>
  :root {
    --brand-blue: #0355a3;
    --brand-red: #ed282f;
    --card-white: #ffffff;
    --backdrop: #e9e8e6;
  }
  * { margin: 0; padding: 0; box-sizing: border-box; }
  html, body { width: 1200px; height: 800px; overflow: hidden; }
  body {
    background: var(--backdrop);
    font-family: "Open Sans", Arial, sans-serif;
    display: flex;
    align-items: center;
    justify-content: center;
    gap: 40px;
  }
  .card {
    position: relative;
    width: 540px;
    height: 309px;
    overflow: hidden;
    box-shadow: 0 6px 18px rgba(0,0,0,0.18);
  }
  .card--back { background: var(--brand-red); }
  .card--front { background: var(--card-white); color: var(--brand-blue); }

  .wordmark {
    font-family: "Nunito Sans", Arial, sans-serif;
    font-weight: 800;
    letter-spacing: -1px;
    line-height: 1;
  }
  .card--back .wordmark {
    position: absolute;
    left: 28px;
    bottom: 38px;
    font-size: 70px;
    color: var(--card-white);
  }
  .card--front .wordmark {
    position: absolute;
    right: 30px;
    top: 42px;
    font-size: 52px;
    color: var(--brand-blue);
  }

  .edge-tab {
    position: absolute;
    width: 8px;
    height: 34px;
    background: var(--brand-red);
  }
  .edge-tab--left { left: 0; top: 62px; }
  .edge-tab--right { right: 0; top: 196px; }

  .holder { position: absolute; left: 28px; top: 62px; }
  .holder__name { font-size: 17px; font-weight: 700; }
  .holder__title { font-size: 13px; margin-top: 0; }

  .address {
    position: absolute;
    left: 28px;
    top: 142px;
    font-size: 14px;
    line-height: 1.3;
    display: flex;
    gap: 6px;
  }

  .rule {
    position: absolute;
    left: 230px;
    right: 0;
    top: 209px;
    height: 4px;
    background: var(--brand-red);
  }
  .rule-mark {
    position: absolute;
    left: 356px;
    top: 181px;
    width: 60px;
    height: 60px;
    border-radius: 50%;
    background: var(--brand-red);
  }

  .contact {
    position: absolute;
    left: 300px;
    top: 248px;
    font-size: 14px;
    line-height: 1.45;
  }
  .contact__row { display: flex; align-items: center; gap: 8px; }
  .icon { width: 13px; height: 13px; flex: none; }
</style>
</head>
<body>
  <section class="card card--back" aria-label="Card back">
    <div class="wordmark">Kelvaro</div>
  </section>

  <section class="card card--front" aria-label="Card front">
    <div class="edge-tab edge-tab--left"></div>
    <div class="edge-tab edge-tab--right"></div>

    <div class="holder">
      <p class="holder__name">Tobias Vrenholt</p>
      <p class="holder__title">CEO</p>
    </div>

    <div class="address">
      <svg class="icon" viewBox="0 0 12 12"><path d="M6 0a4 4 0 0 0-4 4c0 3 4 8 4 8s4-5 4-8a4 4 0 0 0-4-4zm0 5.5A1.5 1.5 0 1 1 6 2.5a1.5 1.5 0 0 1 0 3z" fill="var(--brand-red)"/></svg>
      <p>123, Main Avenue, Any City,<br>NY 10001</p>
    </div>

    <div class="wordmark">Kelvaro</div>

    <div class="rule"></div>
    <div class="rule-mark"></div>

    <div class="contact">
      <p class="contact__row">
        <svg class="icon" viewBox="0 0 12 12"><path d="M2.5 0.5l2 2.5-1.2 1.3c.7 1.6 2 2.9 3.6 3.6L8.2 6.7l2.6 2-1 2.6C5 11 1 7 .7 1.6z" fill="var(--brand-red)"/></svg>
        +46 712 418257
      </p>
      <p class="contact__row">
        <svg class="icon" viewBox="0 0 12 12"><rect x="0" y="2" width="12" height="8" fill="var(--brand-red)"/><path d="M0 2l6 4.5L12 2" stroke="#fff" stroke-width="1" fill="none"/></svg>
        tobias@kelvaro.se
      </p>
    </div>
  </section>
</body>
</html>
```